Post Card (5x7) - Pre-foreclosure Image - Harbor Path Partners

(Two-Sided Post Card)
FACING FORECLOSURE? YOU STILL HAVE OPTIONS.
If you’re behind on payments or at risk of foreclosure, you’re not alone—and it’s not too late to take action.
We help homeowners:
• Explore options to stay in their home
• Stop or delay foreclosure
• Sell quickly for a fair price if needed
No pressure. No obligation. Just real solutions tailored to your situation.
Call - (240) 558-2094
Email - marcus@hpbllc-mail.com
Harbor Path Partners LLC
7200 Bramwick Lane, Ellicott City, MD 21043
**Marcus Fennimore is a Licensed Realtor with Copperleaf Homes Realty in Bethesda, Maryland.
(Leave room for mailing address, return address & postage)
Target Market(s)
Distressed Homeowners
Industry/Entity Type
Real Estate

```html
<!DOCTYPE html>
<html lang="en">
<head>
<meta charset="utf-8">
<title>Harbor Path Partners – Pre-foreclosure Postcard</title>
<link href="https://fonts.googleapis.com/css2?family=Montserrat:wght@400;500;600;800&display=swap" rel="stylesheet">
<style>
  :root {
    --stage: #9e9e9e;
    --paper: #ffffff;
    --ink: #111111;
    --red: #d20a0a;
    --panel: #efefef;
    --rule: #c9c9c9;
    --dusk: #4a5568;
    --sun: #e79a2c;
  }
  * { box-sizing: border-box; margin: 0; padding: 0; }
  html, body { width: 1200px; height: 2400px; overflow: hidden; }
  body {
    background: var(--stage);
    font-family: "Montserrat", sans-serif;
    color: var(--ink);
    position: relative;
  }
  .card {
    position: absolute;
    left: 100px;
    width: 1000px;
    height: 713px;
    overflow: hidden;
    background: var(--paper);
  }
  .card--front { top: 457px; }
  .card--back { top: 1230px; }

  /* Front */
  .front-photo {
    position: absolute; inset: 0;
    background:
      radial-gradient(ellipse 260px 150px at 480px 330px, rgba(231,154,44,.9), rgba(231,154,44,0) 70%),
      linear-gradient(180deg, var(--dusk) 0%, #5e5a55 38%, #2a2a2c 55%, #0d0d0f 100%);
  }
  .brand-name {
    position: absolute; left: 0; right: 0; top: 110px;
    text-align: center; color: #fff;
    font-weight: 500; font-size: 30px; letter-spacing: 5px;
  }
  .brand-name::before {
    content: ""; display: block; width: 22px; height: 22px;
    border: 2px solid #fff; margin: 0 auto 18px;
  }
  .headline-lead {
    position: absolute; left: 0; right: 0; top: 378px;
    text-align: center; color: #fff; font-weight: 500; font-size: 50px;
  }
  .headline-main {
    position: absolute; left: 163px; width: 676px; top: 459px; height: 85px;
    background: var(--red); color: #fff;
    font-weight: 800; font-size: 80px; line-height: 85px; text-align: center;
  }
  .headline-sub {
    position: absolute; left: 0; right: 0; top: 550px;
    text-align: center; color: #fff; font-weight: 500; font-size: 42px;
  }
  .front-body {
    position: absolute; left: 0; right: 0; top: 620px;
    text-align: center; color: #fff; font-size: 18px; line-height: 24px;
  }

  /* Back */
  .help-panel {
    position: absolute; left: 25px; top: 24px; width: 519px; height: 340px;
    background: var(--panel);
  }
  .help-title {
    position: absolute; left: 48px; top: 40px;
    font-weight: 500; font-size: 42px; line-height: 46px;
  }
  .help-title span {
    display: inline-block; background: var(--ink); color: #fff;
    padding: 0 10px; margin-left: -2px;
  }
  .service { position: absolute; top: 152px; width: 150px; font-size: 18px; line-height: 22px; }
  .service__icon {
    width: 58px; height: 58px; border-radius: 50%;
    border: 1.5px solid #bbb; background: #fff;
    display: flex; align-items: center; justify-content: center;
    margin-bottom: 12px;
  }
  .service-link {
    position: absolute; top: 181px; left: 137px; width: 286px; border-top: 1px solid #ccc;
  }
  .promise {
    position: absolute; left: 81px; top: 320px; width: 381px; height: 159px;
    background: #fff; border: 1.5px solid #aaa; border-radius: 18px; text-align: center;
  }
  .promise__tag {
    display: inline-block; margin-top: 38px; background: var(--red); color: #fff;
    font-size: 22px; padding: 2px 8px;
  }
  .promise__text { font-size: 23px; line-height: 30px; margin-top: 12px; }
  .skyline {
    position: absolute; left: 0; top: 500px; width: 566px; height: 213px;
    background: linear-gradient(180deg, #222 0%, #000 25%, #000 100%);
  }
  .contact {
    position: absolute; color: #fff; font-size: 15px; line-height: 19px; white-space: nowrap;
  }
  .contact--phone { left: 70px; top: 588px; }
  .contact--address { left: 300px; top: 580px; padding-left: 20px; }
  .contact-row { display: flex; align-items: center; gap: 6px; height: 24px; }
  .contact--address svg { position: absolute; left: 0; top: 2px; }
  .disclaimer {
    position: absolute; left: 33px; top: 651px; width: 500px; height: 25px;
    border: 1px solid #777; border-radius: 6px; color: #fff;
    font-size: 9px; line-height: 23px; text-align: center; white-space: nowrap; overflow: hidden;
  }
  .return-brand {
    position: absolute; left: 620px; width: 180px; top: 68px;
    text-align: center; font-weight: 500; font-size: 15px; letter-spacing: 2px; line-height: 20px;
  }
  .stamp-box {
    position: absolute; left: 850px; top: 42px; width: 84px; height: 84px; background: var(--panel);
  }
  .address-line {
    position: absolute; left: 634px; width: 288px; border-top: 1px solid var(--rule);
  }
</style>
</head>
<body>

<section class="card card--front">
  <div class="front-photo" role="img" aria-label="City skyline silhouetted against a sunset over a river"></div>
  <div class="brand-name">HARBOR PATH PARTNERS</div>
  <div class="headline-lead">FACING</div>
  <div class="headline-main">FORECLOSURE?</div>
  <div class="headline-sub">YOU STILL HAVE OPTIONS</div>
  <p class="front-body">If you’re behind on payments or at risk of foreclosure, you’re not alone—and<br>it’s not too late to take action.</p>
</section>

<section class="card card--back">
  <div class="help-panel"></div>
  <h2 class="help-title">WE HELP<br><span>HOMEOWNERS</span></h2>
  <div class="service-link"></div>

  <div class="service" style="left:78px">
    <div class="service__icon">
      <svg width="30" height="30" viewBox="0 0 30 30" fill="none" stroke="#222" stroke-width="1.6"><path d="M4 15 L15 5 L26 15"/><path d="M7 13 V26 H23 V13"/><rect x="12" y="18" width="6" height="8"/></svg>
    </div>
    Explore<br>options to stay<br>in their home
  </div>
  <div class="service" style="left:242px">
    <div class="service__icon">
      <svg width="30" height="30" viewBox="0 0 30 30" fill="none" stroke="#222" stroke-width="1.6"><path d="M3 14 L13 5 L23 14"/><path d="M6 12 V25 H16"/><circle cx="21" cy="21" r="6"/><path d="M21 18 V21 H23.5"/></svg>
    </div>
    Stop or<br>delay<br>foreclosure
  </div>
  <div class="service" style="left:393px">
    <div class="service__icon">
      <svg width="30" height="30" viewBox="0 0 30 30" fill="none" stroke="#222" stroke-width="1.6"><circle cx="15" cy="16" r="11"/><circle cx="15" cy="16" r="7"/><circle cx="15" cy="16" r="3"/><path d="M15 2 V5"/></svg>
    </div>
    Sell quickly<br>for a fair price<br>if needed
  </div>

  <div class="promise">
    <span class="promise__tag">No pressure. No obligation.</span>
    <p class="promise__text">Just real solutions tailored to<br>your situation.</p>
  </div>

  <div class="skyline" role="img" aria-label="Black city skyline silhouette"></div>

  <div class="contact contact--phone">
    <div class="contact-row">
      <svg width="13" height="13" viewBox="0 0 24 24" fill="none" stroke="#fff" stroke-width="2"><path d="M5 3 H9 L11 8 L8.5 10 A12 12 0 0 0 14 15.5 L16 13 L21 15 V19 A2 2 0 0 1 19 21 A17 17 0 0 1 3 5 A2 2 0 0 1 5 3 Z"/></svg>
      (240) 558-2094
    </div>
    <div class="contact-row">
      <svg width="14" height="11" viewBox="0 0 24 18" fill="none" stroke="#fff" stroke-width="2"><rect x="1" y="1" width="22" height="16"/><path d="M1 1 L12 10 L23 1"/></svg>
      marcus@hpbllc-mail.com
    </div>
  </div>

  <div class="contact contact--address">
    <svg width="13" height="17" viewBox="0 0 20 26" fill="none" stroke="#fff" stroke-width="2"><path d="M10 25 C4 17 2 13 2 9 A8 8 0 0 1 18 9 C18 13 16 17 10 25 Z"/><circle cx="10" cy="9" r="3"/></svg>
    Harbor Path Partners LLC<br>7200 Bramwick Lane,<br>Ellicott City, MD 21043
  </div>

  <div class="disclaimer">Marcus Fennimore is a Licensed Realtor with Copperleaf Homes Realty in Bethesda, Maryland</div>

  <div class="return-brand">HARBOR PATH<br>PARTNERS</div>
  <div class="stamp-box"></div>
  <div class="address-line" style="top:229px"></div>
  <div class="address-line" style="top:288px"></div>
  <div class="address-line" style="top:350px"></div>
</section>

</body>
</html>
```